Brisk Harbor
Where Your Harbor Counts
Brisk Harbor - Consulting
Creative Brief
Professional
Marlo Fenwick
4817 Tulip Meadow Lane San Diego, CA 92143
briskharbor1@plumetide.com
I would like to have my logo on one side and see a monogram on the front, but all designs are welcome, thanks.

```html
<!DOCTYPE html>
<html lang="en">
<head>
<meta charset="utf-8">
<title>Brisk Harbor – Business Card</title>
<link rel="stylesheet" href="https://fonts.googleapis.com/css2?family=Lato:wght@400;700&family=Cinzel:wght@500&display=swap">
<style>
  :root {
    --backdrop: #ecebe8;
    --card: #ffffff;
    --navy: #1d3f8f;
    --navy-deep: #142d6b;
    --orange: #e8821f;
    --ink: #3f3f3f;
    --shadow: rgba(0, 0, 0, 0.22);
  }
  * { box-sizing: border-box; margin: 0; padding: 0; }
  html, body {
    width: 1200px;
    height: 394px;
    overflow: hidden;
    background: var(--backdrop);
  }
  .sheet {
    position: relative;
    width: 1200px;
    height: 394px;
  }
  .card {
    position: absolute;
    top: 20px;
    width: 564px;
    height: 353px;
    background: var(--card);
    border-radius: 22px;
    box-shadow: 0 3px 10px var(--shadow);
    overflow: hidden;
  }
  .card--front { left: 24px; }
  .card--back { left: 612px; }

  .brand {
    display: flex;
    align-items: center;
    justify-content: center;
    gap: 12px;
    font-family: "Lato", sans-serif;
    font-weight: 700;
    color: var(--navy);
    letter-spacing: 1px;
    text-transform: uppercase;
  }
  .brand__dot {
    width: 16px;
    height: 16px;
    border-radius: 50%;
    background: var(--orange);
  }
  .card--front .brand {
    position: absolute;
    top: 88px;
    left: 0;
    right: 0;
    font-size: 40px;
  }
  .tagline {
    position: absolute;
    top: 142px;
    left: 0;
    right: 0;
    text-align: center;
    font-family: "Cinzel", serif;
    font-weight: 500;
    font-size: 21px;
    letter-spacing: 1px;
    color: var(--orange);
  }
  .contact {
    position: absolute;
    top: 206px;
    left: 0;
    right: 0;
    text-align: center;
    font-family: "Lato", sans-serif;
    font-size: 15px;
    line-height: 27px;
    color: var(--ink);
  }
  .footer-band {
    position: absolute;
    left: 0;
    bottom: 0;
    width: 564px;
    height: 72px;
  }
  .holder-name {
    position: absolute;
    right: 34px;
    bottom: 20px;
    font-family: "Lato", sans-serif;
    font-weight: 700;
    font-size: 18px;
    color: #ffffff;
  }
  .card--back .brand {
    position: absolute;
    top: 0;
    bottom: 0;
    left: 0;
    right: 0;
    font-size: 38px;
  }
</style>
</head>
<body>
<main class="sheet">
  <section class="card card--front">
    <div class="brand"><span class="brand__dot"></span>Brisk Harbor</div>
    <p class="tagline">Where Your Harbor Counts</p>
    <address class="contact">
      4817 Tulip Meadow Lane San Diego, CA 92143<br>
      Email : briskharbor1@plumetide.com
    </address>
    <svg class="footer-band" viewBox="0 0 564 72" aria-hidden="true">
      <rect x="0" y="14" width="564" height="10" fill="var(--orange)"/>
      <path d="M250 24 Q262 18 290 18 L564 18 L564 72 L250 72 Z" fill="var(--navy)"/>
      <path d="M250 24 Q262 18 290 18 L564 18 L564 26 L300 26 Q268 26 250 40 Z" fill="var(--navy-deep)"/>
    </svg>
    <p class="holder-name">Marlo Fenwick</p>
  </section>

  <section class="card card--back">
    <div class="brand"><span class="brand__dot"></span>Brisk Harbor</div>
  </section>
</main>
</body>
</html>
```